Velvet Harbor (A luxury Travel Website)

website text attached in document below

images also attached

feel free to use other images if needed

Target Market(s)

Luxury Seekers and wealthy couples / families

Industry/Entity Type

Luxury Travel

Coding

Coded - Design and coding required

Number of Pages Required

1 page

Requirements
Must have
• A luxury design and easy use.
Nice to have
• Ease of use of page, incorporation of images into the flow of the site

```html
<!DOCTYPE html>
<html lang="en">
<head>
<meta charset="utf-8">
<title>Velvet Harbor — Luxury Travel</title>
<link rel="stylesheet" href="https://fonts.googleapis.com/css2?family=Urbanist:wght@300;400;500;600&family=Playfair+Display:wght@800&display=swap">
<style>
:root{
  --bg:#000;
  --ink:#fff;
  --muted:#d8d8d8;
  --btn:#ececec;
  --btn-ink:#111;
  --accent:#2fb6c9;
  --sea-deep:#0b3f52;
  --sea:#1d7f93;
  --sand:#e9e3d4;
}
*{margin:0;padding:0;box-sizing:border-box}
html,body{width:1200px;height:3824px;overflow:hidden;background:var(--bg)}
body{position:relative;font-family:"Urbanist",sans-serif;color:var(--ink)}
.abs{position:absolute}
.photo{position:absolute}
.btn{position:absolute;background:var(--btn);color:var(--btn-ink);font-size:12px;font-weight:500;
  display:flex;align-items:center;justify-content:center;border-radius:3px;width:124px;height:34px;left:538px}
.nav{position:absolute;top:0;left:0;width:1200px;height:50px;display:flex;align-items:center;z-index:5}
.brand{font-family:"Urbanist",sans-serif;font-size:14px;font-weight:400;letter-spacing:1.5px;color:#b9c6d6;text-transform:uppercase}
.nav-links{position:absolute;display:flex;font-size:10px;font-weight:600;letter-spacing:.4px}
.nav-links span{position:absolute;white-space:nowrap}
.hero{top:0;left:0;width:1200px;height:600px;
  background:linear-gradient(180deg,#000 0,rgba(0,0,0,0) 60px),
  linear-gradient(180deg,rgba(0,0,0,0) 430px,#000 595px),
  radial-gradient(ellipse 380px 300px at 950px 260px,#1f4a22 0,#2c5e2a 50%,rgba(0,0,0,0) 100%),
  radial-gradient(ellipse 300px 200px at 860px 250px,var(--sand) 0,rgba(233,227,212,0) 100%),
  linear-gradient(135deg,var(--sea-deep) 0,var(--sea) 45%,#176a7c 70%,#0f4a55 100%)}
.hero-title{top:258px;left:0;width:1200px;text-align:center;font-family:"Playfair Display",serif;font-weight:800;font-size:36px;line-height:48px}
.rail{left:33px;top:145px;width:2px;height:240px;background:rgba(255,255,255,.45)}
.rail::before{content:"";position:absolute;left:0;top:0;width:2px;height:55px;background:#fff}
.rail-num{left:27px;top:402px;font-size:10px;transform:rotate(-90deg)}
.social{left:1140px;width:14px;height:14px;border-radius:50%;background:var(--ink)}
.center{left:0;width:1200px;text-align:center}
.h-section{font-size:26px;font-weight:400;letter-spacing:.5px}
.lead{font-size:28px;font-weight:400;line-height:37px}
.card{position:absolute;overflow:hidden}
.card-title{position:absolute;left:0;width:100%;text-align:center;font-family:"Playfair Display",serif;font-weight:800;font-size:19px;white-space:nowrap}
.card::after{content:"";position:absolute;left:0;right:0;bottom:0;height:110px;background:linear-gradient(180deg,rgba(0,0,0,0),rgba(0,0,0,.75))}
.card-title{z-index:2}
.footer{top:3320px;left:0;width:1200px;height:504px;
  background:linear-gradient(180deg,#000 0,rgba(0,0,0,0) 120px),
  linear-gradient(180deg,rgba(0,0,0,0) 400px,rgba(0,0,0,.7) 504px),
  radial-gradient(ellipse 180px 160px at 860px 170px,#6b5236 0,rgba(107,82,54,0) 100%),
  linear-gradient(180deg,#7fb3c4 0,#3b8ea8 35%,#1b6f8c 60%,#0e4a66 100%)}
</style>
</head>
<body>

<!-- Hero -->
<div class="photo hero" role="img" aria-label="Aerial view of an island resort with overwater villas on a turquoise lagoon"></div>

<header class="nav">
  <span class="brand abs" style="left:106px;top:17px">Velvet Harbor</span>
  <nav class="nav-links" style="left:0;top:19px">
    <span style="left:252px">DESTINATIONS</span>
    <span style="left:358px">EXPERIENCES</span>
    <span style="left:463px">ABOUT</span>
    <span style="left:532px">GALLERY</span>
  </nav>
  <svg class="abs" style="left:1037px;top:18px" width="14" height="14" viewBox="0 0 14 14" fill="none" stroke="#fff" stroke-width="1.4"><circle cx="6" cy="6" r="4.5"/><path d="M9.5 9.5L13 13"/></svg>
  <svg class="abs" style="left:1070px;top:18px" width="12" height="12" viewBox="0 0 12 12" fill="#fff"><rect x="0" y="0" width="3" height="3"/><rect x="4.5" y="0" width="3" height="3"/><rect x="9" y="0" width="3" height="3"/><rect x="0" y="4.5" width="3" height="3"/><rect x="4.5" y="4.5" width="3" height="3"/><rect x="9" y="4.5" width="3" height="3"/><rect x="0" y="9" width="3" height="3"/><rect x="4.5" y="9" width="3" height="3"/><rect x="9" y="9" width="3" height="3"/></svg>
</header>

<div class="abs rail"></div>
<span class="abs rail-num">01</span>

<h1 class="abs hero-title">Looking to stay at a 5 star<br>hotel or to fly business class anywhere?</h1>
<span class="btn" style="top:383px">Start</span>

<span class="abs social" style="top:274px"></span>
<span class="abs social" style="top:306px"></span>
<span class="abs social" style="top:344px"></span>

<!-- Intro -->
<h2 class="abs center" style="top:558px;font-size:30px;font-weight:400">Explore the World</h2>
<p class="abs center" style="top:620px;font-size:19px;line-height:23px;color:var(--muted)">Share a screenshot of your travel plans and<br>we beat the price, within 24 hours.</p>

<div class="photo" style="left:202px;top:738px;width:375px;height:218px;background:linear-gradient(135deg,#3a2623,#8a6a5e 45%,#d9cfc6 70%,#4b2f2e)" role="img" aria-label="Traveller relaxing in a business class airline seat"></div>
<div class="photo" style="left:624px;top:739px;width:375px;height:218px;background:linear-gradient(180deg,#2f6fb8 0,#4a8ad0 40%,#c96a2a 65%,#1c6b8a 100%)" role="img" aria-label="Resort villa lit at dusk beside a pool under palm trees"></div>

<p class="abs lead" style="left:24px;width:1200px;text-align:center;top:990px">We work directly with hotels and airlines to<br>get you the best price,always.</p>
<span class="btn" style="top:1107px">Add screenshot here</span>

<!-- Experiences -->
<h2 class="abs center h-section" style="top:1268px">EXPERIENCES</h2>

<div class="photo" style="left:94px;top:1417px;width:638px;height:411px;background:linear-gradient(180deg,#b99ad0 0,#e9a9c6 30%,#8f7fb4 55%,#4a7da0 80%,#2b5d7a 100%)" role="img" aria-label="Overwater pavilion with sculpted roof at sunset"></div>
<div class="photo" style="left:647px;top:1353px;width:363px;height:220px;background:linear-gradient(180deg,#9cc8e6 0,#d6eaf3 35%,#5ccbc8 60%,#1fa6b0 100%)" role="img" aria-label="Thatched overwater deck with umbrella over turquoise sea"></div>
<div class="photo" style="left:782px;top:1602px;width:404px;height:323px;background:linear-gradient(180deg,#c98b4a 0,#e8dccd 30%,#cfc2b2 70%,#8e7c6a 100%)" role="img" aria-label="Villa bedroom with canopy bed under a timber roof"></div>
<div class="photo" style="left:273px;top:1789px;width:361px;height:543px;background:linear-gradient(180deg,#c7a473 0,#e8d8bd 30%,#c77f45 55%,#9a7b60 80%,#7c7066 100%)" role="img" aria-label="Lounge with curved sofa beneath a patterned arched window"></div>
<div class="photo" style="left:31px;top:1886px;width:276px;height:366px;background:linear-gradient(180deg,#8fc3ea 0,#cfe6f4 30%,#4fd3cf 55%,#2bb9bb 100%)" role="img" aria-label="Aerial view of overwater villas along a curved jetty"></div>
<div class="photo" style="left:685px;top:1967px;width:254px;height:339px;background:linear-gradient(180deg,#2f5d2a 0,#4b7d3b 40%,#e8e2cf 70%,#45c3bf 100%)" role="img" aria-label="Woven daybed on a palm-lined beach"></div>

<p class="abs lead" style="left:24px;width:1200px;text-align:center;top:2396px;font-size:29px">Tell us about your next holiday plans. The<br>more details the better.</p>
<span class="btn" style="top:2535px">Send Massage</span>

<!-- Gallery -->
<h2 class="abs h-section" style="left:198px;top:2696px">GALLERY</h2>

<div class="card" style="left:194px;top:2783px;width:275px;height:367px;background:linear-gradient(180deg,#8a5a2e 0,#7a9f5a 30%,#c8c3b4 65%,#6a5a48 100%);border-bottom:3px solid var(--accent)" role="img" aria-label="Open-air pavilion overlooking a tropical garden">
  <span class="card-title" style="top:312px;font-size:22px">Coralline Villas &amp; Spa</span>
</div>
<div class="card" style="left:477px;top:2802px;width:247px;height:318px;background:linear-gradient(180deg,#bcd3e0 0,#8a7358 35%,#3fa3b3 65%,#1b5f6f 100%)" role="img" aria-label="Thatched pavilion above a private infinity pool">
  <span class="card-title" style="top:276px">Lumora Maldives,</span>
</div>
<div class="card" style="left:747px;top:2802px;width:246px;height:318px;background:linear-gradient(180deg,#4f9ad6 0,#7fb8e2 30%,#2d6e3e 55%,#2a8fb0 80%,#1b4f66 100%)" role="img" aria-label="Beach club with umbrellas beneath palm trees">
  <span class="card-title" style="top:276px">Azure Reef Laamu</span>
</div>
<div class="card" style="left:1036px;top:2802px;width:200px;height:318px;background:linear-gradient(180deg,#3f86cf 0,#a9cbe8 35%,#2bb0c4 60%,#6a5a48 85%)" role="img" aria-label="Ocean view from a beachfront terrace">
  <span class="card-title" style="top:276px;text-align:left;left:20px">St. Halden Maldives</span>
</div>

<span class="abs" style="left:725px;top:3181px;font-size:10px">01</span>
<span class="abs" style="left:745px;top:3186px;width:254px;height:1px;background:rgba(255,255,255,.6)"></span>
<span class="abs" style="left:745px;top:3185px;width:57px;height:3px;background:#fff"></span>

<!-- Footer -->
<footer>
  <div class="photo footer" role="img" aria-label="Thatched overwater pavilion above a long turquoise infinity pool"></div>
  <nav class="nav-links" style="left:0;top:3785px">
    <span style="left:352px">DESTINATIONS</span>
    <span style="left:460px">EXPERIENCES</span>
    <span style="left:565px">ABOUT</span>
    <span style="left:633px">GALLERY</span>
  </nav>
  <span class="brand abs" style="left:885px;top:3772px;font-size:12px;padding:4px 8px;background:rgba(0,0,0,.55)">Velvet Harbor</span>
</footer>

</body>
</html>
```